BUSINESS CARD FOR GUITAR SCHOOL

I would like to design a business card for my Guitar Music School. The school is called "Pluck & Meadow".

The card should be yellow.

Target Market(s)

18-35 years old

Industry/Entity Type

School

Contact Information for Business Card

I would like to design a business card for my Guitar Music School. The school is called "Pluck & Meadow". The card should be yellow.

Card must be consistent with my website design: www.pluckandmeadow.com.sg

Requirements
Must have
• 1) Name of Company
• 2) Company Logo
• 3) Name of Employee
• 4) Position of Employee
• 5) Contact Number
• 6) Address
Nice to have
• Creative Design
• Card must be consistent with my website design: www.pluckandmeadow.com.sg
Should not have
• Boring Design

```html
<!DOCTYPE html>
<html lang="en">
<head>
<meta charset="UTF-8">
<title>Pluck &amp; Meadow – Business Card</title>
<link rel="stylesheet" href="https://fonts.googleapis.com/css2?family=Cinzel:wght@400&family=Josefin+Sans:wght@300;400;700&display=swap">
<style>
  :root {
    --backdrop: #2f2724;
    --card-yellow: #f6ef1e;
    --card-yellow-deep: #e9df08;
    --contact-yellow: #fff41c;
    --ink: #3b3a36;
    --ink-soft: #55534a;
    --facet-light: #ffd21f;
    --facet-mid: #fbb124;
    --facet-deep: #f0712a;
    --art-tone: rgba(140, 132, 30, .45);
  }
  * { box-sizing: border-box; margin: 0; padding: 0; }
  html, body {
    width: 1200px; height: 864px; overflow: hidden;
    background: var(--backdrop);
  }
  .canvas {
    width: 1200px; height: 864px;
    display: flex; align-items: center; justify-content: center; gap: 40px;
  }
  .card {
    position: relative;
    width: 540px; height: 309px;
    border-radius: 3px;
    overflow: hidden;
    box-shadow: 0 10px 28px rgba(0,0,0,.45);
  }
  .wordmark {
    font-family: "Josefin Sans", sans-serif;
    font-weight: 700;
    color: var(--ink);
    letter-spacing: -0.5px;
    line-height: 1;
    white-space: nowrap;
  }

  /* Front card */
  .card--front {
    background: linear-gradient(160deg, var(--card-yellow) 0%, var(--card-yellow-deep) 100%);
  }
  .card--front .wordmark {
    position: absolute; top: 30px; left: 30px;
    font-size: 30px;
  }
  .guitar-art {
    position: absolute; left: 0; bottom: 0;
    width: 190px; height: 170px;
    background: radial-gradient(ellipse at 30% 70%, var(--art-tone) 0%, rgba(140,132,30,.18) 45%, rgba(140,132,30,0) 75%);
  }
  .tagline {
    position: absolute; left: 195px; top: 178px;
    font-family: "Cinzel", serif;
    font-size: 28px;
    line-height: 1;
    color: var(--ink);
    white-space: nowrap;
  }
  .person {
    position: absolute; left: 197px; top: 230px;
    font-family: "Josefin Sans", sans-serif;
    color: var(--ink);
  }
  .person-name { font-size: 17px; font-weight: 700; letter-spacing: 1px; }
  .person-role { font-size: 13px; font-weight: 400; letter-spacing: 1.5px; margin-top: 4px; color: var(--ink-soft); }

  /* Contact card */
  .card--contact { background: var(--contact-yellow); }
  .facets {
    position: absolute; inset: 0;
    background: linear-gradient(200deg, var(--facet-deep) 0%, var(--facet-mid) 35%, var(--facet-light) 65%, var(--facet-mid) 85%, var(--facet-deep) 100%);
    clip-path: polygon(0 0, 48% 0, 30% 30%, 24% 55%, 14% 82%, 0 100%);
  }
  .card--contact .wordmark {
    position: absolute; top: 26px; right: 28px;
    font-size: 28px;
  }
  .contact-block {
    position: absolute; left: 200px; top: 92px; width: 260px;
    font-family: "Josefin Sans", sans-serif;
    color: var(--ink);
  }
  .contact-title {
    font-weight: 300;
    font-size: 32px;
    letter-spacing: 5px;
    text-align: center;
  }
  .contact-sub {
    font-size: 10px; text-align: center; margin-top: 2px;
    color: var(--ink-soft);
  }
  .rule { border: 0; border-top: 1px solid var(--ink-soft); margin: 4px 0; }
  .contact-note { font-size: 10px; text-align: center; color: var(--ink-soft); white-space: nowrap; }
  .address {
    margin-top: 12px; font-style: normal;
    font-size: 15px; line-height: 1.35; letter-spacing: 1.5px; text-align: center;
  }
  .phone { margin-top: 14px; font-size: 15px; letter-spacing: 2px; text-align: center; }
</style>
</head>
<body>
<main class="canvas">
  <section class="card card--front" aria-label="Business card front">
    <div class="wordmark">Pluck &amp; Meadow</div>
    <div class="guitar-art" role="img" aria-label="Faint illustration of an acoustic guitar"></div>
    <p class="tagline">Every Note Matters</p>
    <div class="person">
      <p class="person-name">Marcus Wen</p>
      <p class="person-role">Head Guitar Instructor</p>
    </div>
  </section>

  <section class="card card--contact" aria-label="Business card contact side">
    <div class="facets" role="img" aria-label="Geometric pattern of orange and yellow triangles"></div>
    <div class="wordmark">Pluck &amp; Meadow</div>
    <div class="contact-block">
      <h2 class="contact-title">CONTACT</h2>
      <p class="contact-sub">Get in touch with us!</p>
      <hr class="rule">
      <p class="contact-note">We are located right beside Brookhaven MRT Station</p>
      <hr class="rule">
      <address class="address">27 Linden Grove Road<br>Heron House B #05-02<br>Singapore 408812</address>
      <p class="phone">Tel: +65 9100 4827</p>
    </div>
  </section>
</main>
</body>
</html>
```